KVO-Business Card Design

I need a modern, professional business card design that includes my logo as the main feature, maybe the entire background with the contact info overlaying or even contact info on the back and the logo full frontal

Neat and organized placement of contact information

Would like to see options in black and white

Target Market(s)

real estate Developers, Construction managers, business and home owners

Industry/Entity Type

Construction

Contact Information for Business Card

KVO Construction
Danny Ferrante
General Contractor

Office: 1-888-902-7315 Ext #1
Cell: 215-730-4162
Fax: 1-888-902-7315

Font styles to use
Serif

Requirements
Must have
• title
• office #
• cell #
• Email
• website
Nice to have
• fax

```html
<!DOCTYPE html>
<html lang="en">
<head>
<meta charset="utf-8">
<title>KVO Construction – Business Cards</title>
<link rel="stylesheet" href="https://fonts.googleapis.com/css2?family=Montserrat:wght@400;500;600;700&display=swap">
<style>
  :root {
    --bg: #ecebe8;
    --card-white: #ffffff;
    --card-black: #0b0b0b;
    --green: #8cc63f;
    --green-dark: #2e8b47;
    --ink: #222222;
    --rule: #1a1a1a;
    --white: #ffffff;
  }
  * { margin: 0; padding: 0; box-sizing: border-box; }
  html, body { width: 1200px; height: 913px; overflow: hidden; }
  body {
    background: var(--bg);
    font-family: "Montserrat", sans-serif;
    position: relative;
  }
  .card {
    position: absolute;
    top: 305px;
    width: 530px;
    height: 303px;
    border-radius: 3px;
    box-shadow: 0 10px 30px rgba(0,0,0,0.18);
  }
  .card--front { left: 45px; background: var(--card-white); }
  .card--back { left: 625px; background: var(--card-black); }

  .brand {
    position: absolute;
    display: flex;
    align-items: center;
    gap: 10px;
    font-weight: 700;
    color: var(--green-dark);
  }
  .brand__mark {
    display: block;
    background: var(--green-dark);
  }
  .card--front .brand { left: 34px; top: 60px; font-size: 24px; }
  .card--front .brand__mark { width: 14px; height: 14px; }

  .holder {
    position: absolute;
    right: 34px;
    top: 48px;
    text-align: right;
    width: 290px;
    border-bottom: 1.5px solid var(--rule);
    padding-bottom: 6px;
  }
  .holder__name { font-size: 22px; font-weight: 500; color: var(--green); }
  .holder__title { font-size: 12px; color: var(--ink); margin-top: 2px; }

  .contacts {
    position: absolute;
    left: 34px;
    bottom: 26px;
    width: 260px;
    border-top: 1.5px solid var(--rule);
    padding-top: 8px;
    list-style: none;
  }
  .contacts li {
    display: flex;
    align-items: center;
    gap: 9px;
    font-size: 12.5px;
    line-height: 20px;
    color: var(--ink);
  }
  .contacts svg { width: 10px; height: 10px; flex: none; fill: var(--green); }

  .card--back .brand {
    left: 0; right: 0; top: 112px;
    justify-content: center;
    font-size: 40px;
    color: var(--green);
  }
  .card--back .brand__mark { width: 22px; height: 22px; background: var(--green); }
  .website {
    position: absolute;
    left: 0; right: 0; top: 176px;
    text-align: center;
    font-size: 15px;
    letter-spacing: 0.5px;
    color: var(--white);
  }
  .website__domain { color: var(--green); }
</style>
</head>
<body>
  <section class="card card--front" aria-label="Business card front">
    <div class="brand"><span class="brand__mark"></span>KVO Construction</div>
    <div class="holder">
      <div class="holder__name">Danny Ferrante</div>
      <div class="holder__title">General Contractor</div>
    </div>
    <ul class="contacts">
      <li><svg viewBox="0 0 10 10"><rect x="2.5" y="0" width="5" height="10" rx="1"/></svg>215-730-4162</li>
      <li><svg viewBox="0 0 10 10"><rect x="1" y="3" width="8" height="6" rx="1"/><rect x="3" y="0" width="4" height="3"/></svg>1-888-902-7315</li>
      <li><svg viewBox="0 0 10 10"><path d="M2 0l2 2.5-1 1.5q1 2 3 3l1.5-1L10 8l-1.5 2Q3 9 0 1.5z"/></svg>1-888-902-7315 Ext #1</li>
      <li><svg viewBox="0 0 10 10"><path d="M0 2h10v6H0z M0 2l5 3.5L10 2" fill="none" stroke="#8cc63f" stroke-width="1.2"/></svg>info@dannyferrante.com</li>
      <li><svg viewBox="0 0 10 10"><circle cx="5" cy="5" r="5"/></svg>www.kvoconstruction.com</li>
    </ul>
  </section>

  <section class="card card--back" aria-label="Business card back">
    <div class="brand"><span class="brand__mark"></span>KVO Construction</div>
    <div class="website">www.<span class="website__domain">kvoconstruction</span>.com</div>
  </section>
</body>
</html>
```